One slide graphic for website

I am designing a series of sliders for my website http://new.quillhartmedia.example

The slide I am trying to create has the following message:

EVERY company is a media company.
Empower yours now!

Learn More >

The ideas I have had for imagery are an office building with the letters 'Every Company is a Media Company' either shone onto the building or letters on the building roof ledge ect.

Aby ideas you may have to improve on this would be appreciated.

The idea behind the slide is to promote a software application which gives marketing professionals the chance to increase their media coverage. The message also encourages companies to create their own news on a number of platforms as the media landscape has changed so much. Look at the blue heron stunt whereby they generated 10 million views on clipvault using PR alone.

Good luck and I look forward to seeing your ideas.

Martin

```html
<!DOCTYPE html>
<html lang="en">
<head>
<meta charset="utf-8">
<title>Every Company is a Media Company – Slide</title>
<link rel="stylesheet" href="https://fonts.googleapis.com/css2?family=Roboto+Condensed:wght@400&family=Open+Sans:wght@400&display=swap">
<style>
  :root {
    --sky-deep: #0a111d;
    --sky-mid: #1d2a40;
    --sky-cloud: #7c8aa0;
    --facade-shadow: #120e09;
    --facade-dark: #2e2518;
    --facade-warm: #6e5639;
    --facade-glow: #b89a6a;
    --facade-bright: #d8c29a;
    --brand-green: #9cc4b3;
    --letter-silver: #e6e8e8;
    --letter-shadow: rgba(0, 0, 0, 0.6);
    --button-bg: #ffffff;
    --button-text: #f7941d;
  }
  html, body {
    margin: 0;
    padding: 0;
    width: 1200px;
    height: 404px;
    overflow: hidden;
    background: var(--sky-deep);
  }
  .slide {
    position: relative;
    width: 1200px;
    height: 404px;
    overflow: hidden;
  }
  .slide__scene {
    position: absolute;
    inset: 0;
    display: block;
  }
  .slide__brand {
    position: absolute;
    left: 240px;
    top: 244px;
    margin: 0;
    font-family: "Roboto Condensed", sans-serif;
    font-weight: 400;
    font-size: 46px;
    line-height: 54px;
    letter-spacing: 5px;
    color: var(--brand-green);
    transform: rotate(-9deg);
    transform-origin: left bottom;
    white-space: nowrap;
  }
  .slide__headline {
    position: absolute;
    left: 538px;
    top: 218px;
    margin: 0;
    font-family: "Roboto Condensed", sans-serif;
    font-weight: 400;
    font-size: 36px;
    line-height: 44px;
    color: var(--letter-silver);
    text-shadow: 1px 3px 0 var(--letter-shadow);
    transform: rotate(-7.5deg);
    transform-origin: left bottom;
    white-space: nowrap;
  }
  .slide__cta {
    position: absolute;
    left: 838px;
    top: 288px;
    width: 277px;
    height: 67px;
    display: flex;
    align-items: center;
    justify-content: center;
    background: var(--button-bg);
    border-radius: 7px;
    font-family: "Open Sans", sans-serif;
    font-size: 29px;
    color: var(--button-text);
    text-decoration: none;
  }
</style>
</head>
<body>
  <section class="slide">
    <svg class="slide__scene" width="1200" height="404" viewBox="0 0 1200 404" role="img" aria-label="Night view of a glass office building with warm lit steel lattice behind its facade, under a dark cloudy sky">
      <defs>
        <linearGradient id="sky" x1="0" y1="0" x2="0.4" y2="1">
          <stop offset="0" stop-color="var(--sky-mid)"/>
          <stop offset="0.6" stop-color="var(--sky-deep)"/>
          <stop offset="1" stop-color="#05080d"/>
        </linearGradient>
        <radialGradient id="cloud" cx="380" cy="10" r="260" gradientUnits="userSpaceOnUse" gradientTransform="translate(380 10) scale(1 0.35) translate(-380 -10)">
          <stop offset="0" stop-color="var(--sky-cloud)" stop-opacity="0.9"/>
          <stop offset="1" stop-color="var(--sky-cloud)" stop-opacity="0"/>
        </radialGradient>
        <linearGradient id="facade" x1="0" y1="0.15" x2="1" y2="0.85">
          <stop offset="0" stop-color="var(--facade-shadow)"/>
          <stop offset="0.3" stop-color="var(--facade-dark)"/>
          <stop offset="0.6" stop-color="var(--facade-warm)"/>
          <stop offset="0.85" stop-color="var(--facade-glow)"/>
          <stop offset="1" stop-color="var(--facade-warm)"/>
        </linearGradient>
        <radialGradient id="glow" cx="850" cy="300" r="420" gradientUnits="userSpaceOnUse">
          <stop offset="0" stop-color="var(--facade-bright)" stop-opacity="0.45"/>
          <stop offset="1" stop-color="var(--facade-bright)" stop-opacity="0"/>
        </radialGradient>
        <linearGradient id="edge" x1="0" y1="0" x2="1" y2="0">
          <stop offset="0" stop-color="#000" stop-opacity="0.75"/>
          <stop offset="0.25" stop-color="#000" stop-opacity="0"/>
        </linearGradient>
      </defs>
      <rect class="scene__sky" width="1200" height="404" fill="url(#sky)"/>
      <rect class="scene__cloud" width="1200" height="404" fill="url(#cloud)"/>
      <polygon class="scene__building" points="40,404 250,150 600,20 640,0 1200,0 1200,404" fill="url(#facade)"/>
      <polygon class="scene__building-glow" points="40,404 250,150 600,20 640,0 1200,0 1200,404" fill="url(#glow)"/>
      <polygon class="scene__building-edge" points="40,404 250,150 600,20 640,0 1200,0 1200,404" fill="url(#edge)"/>
    </svg>
    <p class="slide__brand">QUILLHART</p>
    <h1 class="slide__headline">“Every Company is a Media Company”</h1>
    <a class="slide__cta" href="http://new.quillhartmedia.example">Learn More</a>
  </section>
</body>
</html>
```